Zielgruppe
Wir sind ein Personaldienstleister und vermitteln ausländisches medizinisches Fachpersonal an deutsche Einrichtungen. Unsere Zielgruppe sind Krankenhäuser, Pflegeheime, Ärztehäuser, Praxen, Labore und weitere medizinische Institutionen.
Aufgabenstellung
Wir haben eine Infobroschüre sowie eine PowerPoint Präsentation bereits mit einem groben Design erstellt. Texte und Beispielbilder (Stockmaterial) sind ebenfalls vorhanden, gerne wünschen wir uns auch Eigeninitiative bei der Wahl der Bilder passend zum neuen Design.
Wir wünschen uns ein Redesign mit einem kreativen, einzigartigen Design. Zudem ist uns wichtig, dass unsere Infografiken qualitativ und hochwertig gestaltet werden.
Dieses Projekt ist mit zukünftigen Folgeprojekten verbunden, da wir weitere Präsentationen und Broschüren für andere Zielgruppen benötigen.

```html
<!DOCTYPE html>
<html lang="de">
<head>
<meta charset="utf-8">
<title>Vantoria HR – Broschüre</title>
<link href="https://fonts.googleapis.com/css2?family=Fira+Sans:wght@400;500;600&family=Fira+Sans+Condensed:wght@500;600&display=swap" rel="stylesheet">
<style>
:root{
  --backdrop:#b3b5b5;
  --paper:#ffffff;
  --teal:#1a4047;
  --green:#3d8a6f;
  --mint:#c9e6dc;
  --rail:#cfd2d2;
  --ink:#3a3f40;
}
*{margin:0;padding:0;box-sizing:border-box}
html,body{width:911px;height:1200px;overflow:hidden;background:var(--backdrop)}
body{font-family:"Fira Sans",sans-serif;color:var(--ink)}
.board{position:absolute;left:0;top:0;width:1679px;height:2212px;transform:scale(0.54258);transform-origin:0 0;background:var(--backdrop)}
.page{position:absolute;background:var(--paper)}
.abs{position:absolute}
.footer-band{position:absolute;background:var(--teal);color:#fff;font-size:13px;display:flex;align-items:center}
.footer-band span{position:absolute}
.page-title{position:absolute;color:var(--teal);font-weight:600;white-space:nowrap}

/* process steps */
.step{position:absolute;width:240px;height:170px}
.step svg.frame{position:absolute;left:0;top:0;overflow:visible}
.step-num{position:absolute;font-family:"Fira Sans Condensed",sans-serif;font-weight:600;font-size:30px;color:var(--teal);line-height:1}
.step-text{position:absolute;font-size:8.6px;line-height:1.22;color:var(--ink);width:170px}

/* timeline */
.tl-text{position:absolute;width:218px;font-size:10.6px;line-height:1.24;text-align:justify;color:var(--ink)}
.tl-text b{display:block;color:var(--teal);font-weight:500;font-size:11px}

.teal-panel{position:absolute;background:var(--teal);color:#fff}
.photo{position:absolute}
</style>
</head>
<body>
<svg width="0" height="0" style="position:absolute">
  <defs>
    <symbol id="ic-form" viewBox="0 0 60 60"><g fill="none" stroke="#1a4047" stroke-width="2.4" stroke-linecap="round"><rect x="10" y="6" width="34" height="46" rx="3"/><path d="M17 17h4M25 17h13M17 26h4M25 26h13M17 35h4M25 35h8"/><path d="M36 48l14-14 4 4-14 14h-4z"/></g></symbol>
    <symbol id="ic-de" viewBox="0 0 60 60"><path d="M30 28c10 0 18 6 18 13 0 3-1 5-3 7l3 6-8-3c-3 1-6 2-10 2" fill="#1a4047"/><ellipse cx="24" cy="24" rx="20" ry="15" fill="#fff" stroke="#1a4047" stroke-width="2.4"/><path d="M14 36l-4 8 10-5" fill="#fff" stroke="#1a4047" stroke-width="2.4"/><text x="24" y="29" text-anchor="middle" font-family="Fira Sans" font-size="14" fill="#1a4047">DE</text></symbol>
    <symbol id="ic-copy" viewBox="0 0 60 60"><g fill="none" stroke="#1a4047" stroke-width="2.4" stroke-linejoin="round"><path d="M12 14h18l8 8v30H12z"/><path d="M22 6h18l8 8v30H38"/><path d="M40 6v8h8"/></g></symbol>
    <symbol id="ic-care" viewBox="0 0 60 60"><g fill="#1a4047"><circle cx="23" cy="16" r="5"/><circle cx="37" cy="16" r="5"/><path d="M15 32c0-6 4-9 8-9s8 3 8 9zM29 32c0-6 4-9 8-9s8 3 8 9z"/></g><g fill="none" stroke="#1a4047" stroke-width="2.4" stroke-linecap="round"><path d="M4 26l8 16 12 8h4M56 26l-8 16-12 8h-4"/></g></symbol>
    <symbol id="ic-meet" viewBox="0 0 60 60"><g fill="#1a4047"><rect x="18" y="34" width="24" height="3"/><rect x="29" y="37" width="2" height="14"/><circle cx="12" cy="26" r="4"/><circle cx="48" cy="26" r="4"/><path d="M7 32h10v10H7zM43 32h10v10H43z"/><path d="M6 44h4v8H6zM50 44h4v8h-4z"/></g><g fill="none" stroke="#1a4047" stroke-width="2"><rect x="18" y="6" width="10" height="8" rx="2"/><circle cx="38" cy="11" r="5"/></g></symbol>
    <symbol id="ic-docs" viewBox="0 0 60 60"><g fill="none" stroke="#1a4047" stroke-width="2.4"><rect x="8" y="14" width="30" height="38"/><rect x="18" y="6" width="34" height="38" fill="#c9e6dc"/><path d="M25 16h20M25 23h20M25 30h20M25 37h12"/></g></symbol>
    <symbol id="ic-house" viewBox="0 0 60 60"><path d="M8 28L30 10l22 18" fill="none" stroke="#1a4047" stroke-width="3"/><path d="M14 26v26h32V26L30 14z" fill="#1a4047"/><rect x="26" y="38" width="8" height="14" fill="#c9e6dc"/><rect x="18" y="32" width="6" height="6" fill="#c9e6dc"/><rect x="36" y="32" width="6" height="6" fill="#c9e6dc"/><rect x="26" y="24" width="8" height="6" fill="#c9e6dc"/><rect x="40" y="10" width="5" height="10" fill="#1a4047"/></symbol>
    <symbol id="ic-travel" viewBox="0 0 60 60"><g fill="#1a4047"><rect x="6" y="30" width="18" height="16" rx="3"/><rect x="12" y="25" width="6" height="5"/><circle cx="40" cy="10" r="5"/><path d="M34 18h10l4 14-4 2-3-8-4 10 6 12h-5l-6-12-2 12h-5l4-20z"/><rect x="4" y="50" width="52" height="3"/></g></symbol>
    <symbol id="ic-person" viewBox="0 0 60 60"><g fill="#1a4047"><circle cx="30" cy="20" r="11"/><path d="M10 54c0-13 9-20 20-20s20 7 20 20z"/></g><path d="M28 14h4M30 12v4" stroke="#fff" stroke-width="2"/></symbol>
    <symbol id="ic-puzzle" viewBox="0 0 60 60"><g fill="none" stroke="#1a4047" stroke-width="2.4" stroke-linejoin="round"><path d="M30 28h8a5 5 0 1 1 8 0h6v24H30v-8a5 5 0 1 0 0-8z"/><path d="M8 14l14-6 3 7a5 5 0 1 1 7 3l3 7-14 6-3-7a5 5 0 1 0-7 3z"/></g></symbol>
    <symbol id="ic-contact" viewBox="0 0 60 60"><g fill="none" stroke="#1a4047" stroke-width="3"><rect x="10" y="8" width="34" height="44" rx="3"/><circle cx="27" cy="24" r="6"/><path d="M17 40c2-7 18-7 20 0"/><path d="M44 16h6v8h-6M44 28h6v8h-6"/></g></symbol>
    <symbol id="ic-contract" viewBox="0 0 60 60"><g fill="#1a4047"><path d="M10 6h26l10 10v36H10z"/></g><g stroke="#fff" stroke-width="3"><path d="M16 22h14M16 30h18M16 38h12"/></g><path d="M36 48l14-14 5 5-14 14h-5z" fill="#fff" stroke="#1a4047" stroke-width="2.5"/></symbol>
    <symbol id="ic-group" viewBox="0 0 60 60"><g fill="none" stroke="#1a4047" stroke-width="2.6"><circle cx="30" cy="26" r="5"/><circle cx="16" cy="32" r="5"/><circle cx="44" cy="32" r="5"/><path d="M20 46c1-8 19-8 20 0M6 52c1-8 18-8 20 0M34 52c1-8 18-8 20 0"/><path d="M24 10l4 4 8-8"/></g></symbol>
    <symbol id="ic-select" viewBox="0 0 60 60"><g fill="none" stroke="#1a4047" stroke-width="2"><circle cx="30" cy="28" r="6"/><path d="M20 44c2-8 18-8 20 0"/><circle cx="10" cy="10" r="3"/><circle cx="50" cy="10" r="3"/><circle cx="10" cy="50" r="3"/><circle cx="50" cy="50" r="3"/><path d="M16 10h6M38 10h6M10 16v6M50 16v6M10 38v6M50 38v6M16 50h6M38 50h6"/></g></symbol>
    <symbol id="ic-shake" viewBox="0 0 60 60"><g fill="none" stroke="#c9e6dc" stroke-width="3.5" stroke-linejoin="round" stroke-linecap="round"><path d="M4 22l10-6 10 4 8-4 8 2 16 4 4 10"/><path d="M8 34l14 14 6 2 4-4 4 2 4-4 4 0 8-10"/><path d="M32 20l-8 8 4 4 8-6"/></g></symbol>
  </defs>
</svg>

<div class="board">

  <!-- Page 1: Rekrutierungsverfahren -->
  <section class="page" style="left:97px;top:68px;width:743px;height:1044px">
    <h1 class="page-title" style="left:91px;top:34px;font-size:44px">Unser Rekrutierungsverfahren</h1>
  </section>

  <div class="abs" style="left:0;top:0">
    <div class="step" style="left:366px;top:209px">
      <svg class="frame" width="240" height="170"><path d="M22 0H0v152h32" fill="none" stroke="#1a4047" stroke-width="1.4" stroke-dasharray="3 3"/><circle cx="25" cy="0" r="7" fill="#1a4047"/><circle cx="32" cy="152" r="7" fill="#1a4047"/><circle cx="97" cy="24" r="52" fill="#c9e6dc"/><path d="M60 -16a62 62 0 0 1 85 10M150 56a62 62 0 0 1 -60 30" fill="none" stroke="#1a4047" stroke-width="1.4"/><use href="#ic-form" x="69" y="-4" width="56" height="56"/></svg>
      <div class="step-num" style="left:6px;top:95px">01</div>
      <div class="step-text" style="left:43px;top:92px">Bewerber:in wird auf uns aufmerksam, füllt unser Bewerbungsformular aus und reicht die nötigen Dokumente ein.</div>
    </div>

    <div class="step" style="left:145px;top:420px">
      <svg class="frame" width="240" height="170"><path d="M25 0H0v155h28" fill="none" stroke="#1a4047" stroke-width="1.4" stroke-dasharray="3 3"/><circle cx="25" cy="0" r="7" fill="#1a4047"/><circle cx="28" cy="155" r="7" fill="#1a4047"/><circle cx="98" cy="25" r="52" fill="#c9e6dc"/><path d="M61 -15a62 62 0 0 1 85 10M151 57a62 62 0 0 1 -60 30" fill="none" stroke="#1a4047" stroke-width="1.4"/><use href="#ic-de" x="70" y="-3" width="56" height="56"/></svg>
      <div class="step-num" style="left:5px;top:95px">02</div>
      <div class="step-text" style="left:42px;top:93px">Um das erforderliche Sprachniveau B2 zu erreichen, bieten wir Bewerber:innen kostenlose interne Sprachkurse an.</div>
    </div>

    <div class="step" style="left:360px;top:406px">
      <svg class="frame" width="240" height="170"><path d="M25 0H0v169h25" fill="none" stroke="#1a4047" stroke-width="1.4" stroke-dasharray="3 3"/><circle cx="25" cy="0" r="7" fill="#1a4047"/><circle cx="25" cy="169" r="7" fill="#1a4047"/><circle cx="97" cy="26" r="52" fill="#c9e6dc"/><path d="M60 -14a62 62 0 0 1 85 10M150 58a62 62 0 0 1 -60 30" fill="none" stroke="#1a4047" stroke-width="1.4"/><use href="#ic-copy" x="69" y="-2" width="56" height="56"/></svg>
      <div class="step-num" style="left:6px;top:95px">03</div>
      <div class="step-text" style="left:42px;top:93px">Parallel zu ihren sprachlichen Vorbereitungen beginnen die Bewerber:innen mit dem Anerkennungsprozess.</div>
    </div>

    <div class="step" style="left:603px;top:429px">
      <svg class="frame" width="240" height="170"><path d="M25 0H0v146h33" fill="none" stroke="#1a4047" stroke-width="1.4" stroke-dasharray="3 3"/><circle cx="25" cy="0" r="7" fill="#1a4047"/><circle cx="33" cy="146" r="7" fill="#1a4047"/><circle cx="97" cy="16" r="52" fill="#c9e6dc"/><path d="M60 -24a62 62 0 0 1 85 10M150 48a62 62 0 0 1 -60 30" fill="none" stroke="#1a4047" stroke-width="1.4"/><use href="#ic-care" x="69" y="-12" width="56" height="56"/></svg>
      <div class="step-num" style="left:6px;top:83px">04</div>
      <div class="step-text" style="left:45px;top:82px">Wir bereiten unsere Kandidat:innen auf die bevorstehenden Videointerviews vor und erarbeiten proaktive Lösungen für Situationen, die während des Vorstellungs­gesprächs auftreten können.</div>
    </div>

    <div class="step" style="left:147px;top:635px">
      <svg class="frame" width="240" height="170"><path d="M25 0H0v150h25" fill="none" stroke="#1a4047" stroke-width="1.4" stroke-dasharray="3 3"/><circle cx="25" cy="0" r="7" fill="#1a4047"/><circle cx="25" cy="150" r="7" fill="#1a4047"/><circle cx="97" cy="15" r="52" fill="#c9e6dc"/><path d="M60 -25a62 62 0 0 1 85 10M150 47a62 62 0 0 1 -60 30" fill="none" stroke="#1a4047" stroke-width="1.4"/><use href="#ic-meet" x="69" y="-13" width="56" height="56"/></svg>
      <div class="step-num" style="left:5px;top:90px">05</div>
      <div class="step-text" style="left:46px;top:86px;width:140px">Die Bewerber:innen haben Vorstellungsgespräche mit potenziellen Arbeitgebern aus Deutschland. Wir begleiten Sie dabei.</div>
    </div>

    <div class="step" style="left:362px;top:637px">
      <svg class="frame" width="240" height="170"><path d="M25 0H0v148h27" fill="none" stroke="#1a4047" stroke-width="1.4" stroke-dasharray="3 3"/><circle cx="25" cy="0" r="7" fill="#1a4047"/><circle cx="27" cy="148" r="7" fill="#1a4047"/><circle cx="97" cy="13" r="52" fill="#c9e6dc"/><path d="M60 -27a62 62 0 0 1 85 10M150 45a62 62 0 0 1 -60 30" fill="none" stroke="#1a4047" stroke-width="1.4"/><use href="#ic-docs" x="69" y="-15" width="56" height="56"/></svg>
      <div class="step-num" style="left:6px;top:105px">06</div>
      <div class="step-text" style="left:42px;top:87px">Bei erfolgreicher Einigung kommt es zur Unterzeichnung eines Arbeitsvertrags. Wir kümmern uns um die weiteren Prozessa­bläufe.</div>
    </div>

    <div class="step" style="left:600px;top:635px">
      <svg class="frame" width="240" height="170"><path d="M25 0H0v151h31" fill="none" stroke="#1a4047" stroke-width="1.4" stroke-dasharray="3 3"/><circle cx="25" cy="0" r="7" fill="#1a4047"/><circle cx="31" cy="151" r="7" fill="#1a4047"/><circle cx="97" cy="22" r="52" fill="#c9e6dc"/><path d="M60 -18a62 62 0 0 1 85 10M150 54a62 62 0 0 1 -60 30" fill="none" stroke="#1a4047" stroke-width="1.4"/><use href="#ic-house" x="69" y="-6" width="56" height="56"/></svg>
      <div class="step-num" style="left:7px;top:98px">07</div>
      <div class="step-text" style="left:43px;top:93px">Die für die Beschäftigung in Deutschland erforderlichen Dokumente werden von uns erstellt bzw. eingeholt und wir suchen eine Unterkunft in der Nähe des künftigen Arbeitsortes.</div>
    </div>

    <div class="step" style="left:150px;top:845px">
      <svg class="frame" width="240" height="170"><path d="M25 0H0v150h25" fill="none" stroke="#1a4047" stroke-width="1.4" stroke-dasharray="3 3"/><circle cx="25" cy="0" r="7" fill="#1a4047"/><circle cx="25" cy="150" r="7" fill="#1a4047"/><circle cx="97" cy="22" r="52" fill="#c9e6dc"/><path d="M60 -18a62 62 0 0 1 85 10M150 54a62 62 0 0 1 -60 30" fill="none" stroke="#1a4047" stroke-width="1.4"/><use href="#ic-travel" x="69" y="-6" width="56" height="56"/></svg>
      <div class="step-num" style="left:6px;top:97px">08</div>
      <div class="step-text" style="left:43px;top:93px">Einreise Ihres/r neune Mitarbeiter:in nach Deutschland. Wir organisieren die Abholung vom Flughafen und den Transport zur Unterkunft.</div>
    </div>

    <div class="step" style="left:364px;top:845px">
      <svg class="frame" width="240" height="170"><path d="M25 0H0v150h25" fill="none" stroke="#1a4047" stroke-width="1.4" stroke-dasharray="3 3"/><circle cx="25" cy="0" r="7" fill="#1a4047"/><circle cx="25" cy="150" r="7" fill="#1a4047"/><circle cx="99" cy="22" r="52" fill="#c9e6dc"/><path d="M62 -18a62 62 0 0 1 85 10M152 54a62 62 0 0 1 -60 30" fill="none" stroke="#1a4047" stroke-width="1.4"/><use href="#ic-person" x="71" y="-6" width="56" height="56"/></svg>
      <div class="step-num" style="left:6px;top:97px">09</div>
      <div class="step-text" style="left:43px;top:93px;width:145px">Wir bereiten Ihre neue Fachkraft auf den Arbeitsantritt vor und begleiten sie zum ersten Arbeitstag.</div>
    </div>

    <div class="step" style="left:600px;top:847px">
      <svg class="frame" width="240" height="170"><path d="M25 0H0v148h25" fill="none" stroke="#1a4047" stroke-width="1.4" stroke-dasharray="3 3"/><circle cx="25" cy="0" r="7" fill="#1a4047"/><circle cx="25" cy="148" r="7" fill="#1a4047"/><circle cx="97" cy="23" r="52" fill="#c9e6dc"/><path d="M60 -17a62 62 0 0 1 85 10M150 55a62 62 0 0 1 -60 30" fill="none" stroke="#1a4047" stroke-width="1.4"/><use href="#ic-puzzle" x="69" y="-5" width="56" height="56"/></svg>
      <div class="step-num" style="left:7px;top:93px">10</div>
      <div class="step-text" style="left:42px;top:91px;width:160px">Unsere Kandidat:innen werden während der gesamten Probe-/Einarbeitungszeit von uns unterstützt und betreut.</div>
    </div>
  </div>

  <div class="footer-band" style="left:105px;top:1073px;width:727px;height:32px">
    <span style="left:81px">+49 000 123 45 678</span>
    <span style="left:322px">hr@vantoria.example</span>
    <span style="left:527px">www.vantoria-hr.example</span>
  </div>

  <!-- Page 2: Kosten -->
  <section class="page" style="left:855px;top:68px;width:743px;height:1044px"></section>
  <div class="photo" role="img" aria-label="Foto: Geschäftsgespräch mit Handschlag am Besprechungstisch mit Laptops und Kaffeebechern" style="left:862px;top:75px;width:730px;height:480px;background:linear-gradient(180deg,#d6d6d3 0%,#c4c3bf 100%)"></div>
  <div class="teal-panel" style="left:862px;top:555px;width:730px;height:550px">
    <h2 style="position:absolute;left:44px;top:84px;font-size:29px;font-weight:500;line-height:1.22">Was kostet eine gute und faire<br>Rekrutierung bei uns?</h2>
    <div style="position:absolute;left:38px;top:176px;width:665px;font-size:15.5px;line-height:1.24">
      <p>Wir bei Vantoria HR legen großen Wert auf Kundenzufriedenheit. Mit unserem 360°-Service decken wir alle wichtigen Serviceleistungen rund um die Rekrutierung von ausländischen Fachkräften ab und bieten Ihnen dadurch noch mehr Flexibilität und Dynamik.</p>
      <p style="margin-top:19px">Bei der Berechnung unserer Preise spielen somit viele Faktoren eine wichtige Rolle und sind stark abhängig vom Leistungsumfang und der Art der Rekrutierung.</p>
      <p style="margin-top:19px">Preisangebote kalkulieren wir individuell und Bedarfsgerecht erst mit einer konkreten und detaillierten Nachfrage.</p>
      <p style="margin-top:19px">Teilen Sie uns jetzt Ihren Personalbedarf mit!</p>
    </div>
  </div>

  <!-- Page 3: 6 Schritte -->
  <section class="page" style="left:97px;top:1135px;width:743px;height:1045px">
    <h1 class="page-title" style="left:83px;top:62px;font-size:35px">In 6 Schritten zu Ihrer neuen Fachkraft</h1>
  </section>

  <svg class="abs" style="left:0;top:0" width="1679" height="2212">
    <rect x="467" y="1334" width="9" height="598" fill="var(--rail)"/>
    <rect x="398" y="1328" width="30" height="12" fill="#3d8a6f"/><rect x="515" y="1328" width="135" height="12" fill="#3d8a6f"/>
    <circle cx="380" cy="1334" r="19" fill="#1a4047"/>
    <circle cx="677" cy="1334" r="28" fill="#fff" stroke="#1a4047" stroke-width="7"/>
    <circle cx="471" cy="1334" r="48" fill="#fff" stroke="#1a4047" stroke-width="9"/>
    <use href="#ic-contact" x="449" y="1312" width="44" height="44"/>
    <rect x="293" y="1446" width="135" height="12" fill="#1a4047"/><rect x="515" y="1446" width="35" height="12" fill="#1a4047"/>
    <circle cx="265" cy="1452" r="28" fill="#fff" stroke="#3d8a6f" stroke-width="7"/>
    <circle cx="563" cy="1452" r="19" fill="#3d8a6f"/>
    <circle cx="471" cy="1452" r="48" fill="#fff" stroke="#3d8a6f" stroke-width="9"/>
    <use href="#ic-contract" x="449" y="1430" width="44" height="44"/>
    <rect x="398" y="1563" width="30" height="12" fill="#1a4047"/><rect x="515" y="1563" width="135" height="12" fill="#1a4047"/>
    <circle cx="380" cy="1569" r="19" fill="#c9e6dc"/>
    <circle cx="677" cy="1569" r="28" fill="#fff" stroke="#c9e6dc" stroke-width="7"/>
    <circle cx="471" cy="1569" r="48" fill="#fff" stroke="#c9e6dc" stroke-width="9"/>
    <use href="#ic-group" x="449" y="1547" width="44" height="44"/>
    <rect x="293" y="1681" width="135" height="12" fill="#3d8a6f"/><rect x="515" y="1681" width="35" height="12" fill="#3d8a6f"/>
    <circle cx="265" cy="1687" r="28" fill="#fff" stroke="#1a4047" stroke-width="7"/>
    <circle cx="563" cy="1687" r="19" fill="#1a4047"/>
    <circle cx="471" cy="1687" r="48" fill="#fff" stroke="#1a4047" stroke-width="9"/>
    <use href="#ic-meet" x="449" y="1665" width="44" height="44"/>
    <rect x="398" y="1799" width="30" height="12" fill="#c9e6dc"/><rect x="515" y="1799" width="135" height="12" fill="#c9e6dc"/>
    <circle cx="380" cy="1805" r="19" fill="#3d8a6f"/>
    <circle cx="677" cy="1805" r="28" fill="#fff" stroke="#3d8a6f" stroke-width="7"/>
    <circle cx="471" cy="1805" r="48" fill="#fff" stroke="#3d8a6f" stroke-width="9"/>
    <use href="#ic-select" x="449" y="1783" width="44" height="44"/>
    <rect x="293" y="1926" width="135" height="12" fill="#3d8a6f"/><rect x="515" y="1926" width="35" height="12" fill="#3d8a6f"/>
    <circle cx="265" cy="1932" r="28" fill="#fff" stroke="#1a4047" stroke-width="7"/>
    <circle cx="563" cy="1932" r="19" fill="#1a4047"/>
    <circle cx="471" cy="1932" r="52" fill="#1a4047"/>
    <use href="#ic-shake" x="445" y="1906" width="52" height="52"/>
    <g font-family="Fira Sans" font-weight="600" font-size="24" fill="#1a4047" text-anchor="middle">
      <text x="677" y="1343">1</text><text x="265" y="1461">2</text><text x="677" y="1578">3</text>
      <text x="265" y="1696">4</text><text x="677" y="1814">5</text><text x="265" y="1941">6</text>
    </g>
  </svg>

  <div class="tl-text" style="left:127px;top:1303px"><b>Kontaktaufnahme</b>Sie nehmen Kontakt zu uns auf und teilen uns Ihren Personalbedarf, sowie spezielle Stellenanforderungen mit.</div>
  <div class="tl-text" style="left:599px;top:1428px;width:193px"><b>Vertragsmodalitäten</b>Wir setzen uns mit Ihnen zusammen, besprechen die Einzelheiten und klären die Rahmenbedingungen, individuell auf Sie zugeschnitten.</div>
  <div class="tl-text" style="left:127px;top:1538px"><b>Kandidatenvorauswahl</b>Wir lassen Ihnen vorab übersichtliche CV’s potenzieller Kandidat:innen zukommen und Sie treffen eine Vorauswahl bzw. teilen uns eventuelle Anpassungswünsche mit.</div>
  <div class="tl-text" style="left:599px;top:1661px;width:210px"><b>Vorstellungsgespräche</b>Sie führen die Vorstellungsgespräche mit den Kandidat:innen durch. Unsere Expert:in­nen begleiten Sie dabei als wichtiges Binde­glied, um bei Missverständnissen und Unklarheiten vorzubeugen.</div>
  <div class="tl-text" style="left:127px;top:1784px"><b>Finale Personalauswahl</b>Sie entscheiden sich für Ihre Wunschmi­tarbeiter:innen - wir stellen Ihnen zusammen mit einer persönlichen Einschätzung zu den jeweiligen Kandidat:innen alle Informationen und Unterlagen in einem übersichtlichen und informativen Bericht zur Verfügung.</div>
  <div class="tl-text" style="left:599px;top:1906px;width:195px"><b>Arbeitsvertrag</b>Nach Klärung aller wichtigen Modal­itäten und Besonderheiten unterschrei­bt der/die Bewerber:in seinen/ihren Arbeitsvertrag.</div>

  <h2 class="abs" style="left:127px;top:2015px;font-size:22px;font-weight:500;color:var(--teal)">Erster Arbeitstag</h2>
  <p class="abs" style="left:127px;top:2053px;width:685px;font-size:11.6px;line-height:1.26;color:var(--ink)">Wir begleiten und betreuen unsere Kandidat:innen über den kompletten Auswahlprozess hinweg bis zum Ende ihrer Probezeit. Nicht selten können wir auch nach der erfolgreichen Vermittlung noch wertvolle Klärungs- und Motivationsarbeit leisten. Außerdem übernehmen wir sowohl Abschlussgespräche, als auch die gesamte Korrespondenz mit allen Bewerber:innen, die am Auswahlverfahren beteiligt waren.</p>

  <div class="footer-band" style="left:105px;top:2141px;width:727px;height:32px">
    <span style="left:81px">+49 000 123 45 678</span>
    <span style="left:322px">hr@vantoria.example</span>
    <span style="left:527px">www.vantoria-hr.example</span>
  </div>

  <!-- Page 4: Talentpool -->
  <section class="page" style="left:848px;top:1135px;width:742px;height:1045px"></section>
  <div class="teal-panel" style="left:855px;top:1143px;width:728px;height:1030px">
    <h2 style="position:absolute;left:0;width:100%;top:36px;text-align:center;font-size:34px;font-weight:500">Unser Talentpool</h2>
    <p style="position:absolute;left:34px;width:660px;top:92px;text-align:center;font-size:17.6px;line-height:20.6px">Gesundheits- und Krankenpfleger:in I Pflegefachmann /-frau I Pflegefachassistent:in I Altenpfleger:in I Arzt/Ärztin I Hebamme I Anästhesietechnische:r Assistent:in (ATA) I Operationstechnische:r Assistent:in (OTA) I Medizinisch-technische:r Laborassistent:in (MTLA) I Medizinisch-technische:r Radiologieassistentin (MTRA) I Pflegehilfskräfte I Pflegefachassistent:in I Notfallsanitäter:in I Rettungssanitäter:in I Physiotherapeut:innen I</p>
    <p style="position:absolute;left:0;width:100%;top:236px;text-align:center;font-size:17.6px">… und viele weitere medizinische Berufe.</p>
    <div class="photo" role="img" aria-label="Foto: Pflegekraft in blauer Kleidung, die mit beiden Händen zur Seite zeigt" style="left:75px;top:280px;width:580px;height:750px;background:linear-gradient(180deg,#1f4a52 0%,#245a70 100%)"></div>
  </div>

</div>
</body>
</html>
```